Fold up small biz card size flyer for Waxing Salon

To design a simple informative flyer which can fold 3 times measuring 2" x 9" for Waxing Salon in Toronto ON CanadaMy client would like both sides of flyer to have text i.e. the first half of flyer text on front and second half with address etc on back.She doesn;t want a company name as yet but would like maybe the simple shape of a body as in this sample deisign with a stone background.the other pics are just samples of ideas she has suggessted and if there is any text it should simply be wax or waxing or maybe body waxing.Please don't hesitate to ask quesition and i look forward to your submissions.

Target Market(s)

women amd men of all adult ages

Font styles to use
Serif
Sans Serif
Decorative
Script

Colors

Designer to choose colors to be used in the design.

Requirements
Must have
• Fold into three to biz card size so PLEASE STRICTLY 2 INCHES X 9 INCHES AND FOLDED DOWN TO A 2 X 3 BIZ CARD
• Due to small size of flyer there will have to be text on back as well
• thanks for your time and patience
Nice to have
• the images are simply ideas of existing brands...just stone background with perhadps small body shaped graphic no company name
Should not have
• scanitly clad women preferably small body shoped graphic only please/

```html
<!DOCTYPE html>
<html lang="en">
<head>
<meta charset="utf-8">
<title>Body Waxing Flyer</title>
<link rel="stylesheet" href="https://fonts.googleapis.com/css2?family=Kaushan+Script&family=Poppins:wght@400;600&display=swap">
<style>
  :root {
    --pink-deep: #ef93b5;
    --pink-mid: #f4a9c5;
    --pink-light: #f7b8cf;
    --ink: #5b3a47;
    --line: rgba(255, 235, 243, 0.75);
    --shape: rgba(255, 220, 233, 0.55);
  }
  * { margin: 0; padding: 0; box-sizing: border-box; }
  html, body { width: 1200px; height: 2699px; overflow: hidden; }
  body {
    position: relative;
    font-family: "Poppins", sans-serif;
    color: var(--ink);
    background: linear-gradient(180deg, var(--pink-deep) 0%, var(--pink-mid) 25%, var(--pink-light) 50%, var(--pink-mid) 75%, var(--pink-deep) 100%);
  }
  .panel-divider {
    position: absolute; left: 602px; top: 0; width: 2px; height: 2699px;
    background: var(--line);
  }
  .block { position: absolute; }
  .script { font-family: "Kaushan Script", cursive; font-weight: 400; }
  .deal-title { left: 97px; top: 78px; font-size: 58px; }
  .offer { left: 120px; top: 266px; font-size: 31px; line-height: 40px; }
  .offer-title { font-size: 40px; font-weight: 600; line-height: 52px; }
  .offer-value { font-size: 40px; font-weight: 600; margin-top: 10px; }
  .figure-art {
    left: 800px; top: 94px; width: 206px; height: 278px;
    background: radial-gradient(ellipse at 50% 45%, var(--shape) 0%, rgba(255,220,233,0) 70%);
  }
  .call-to-action {
    left: 603px; top: 430px; width: 597px; text-align: center;
    font-size: 60px; line-height: 86px;
  }
  .body-outline {
    position: absolute; width: 596px; height: 190px;
    background: linear-gradient(180deg, rgba(255,230,240,0) 0%, rgba(255,230,240,0.28) 50%, rgba(255,230,240,0) 100%);
  }
  .guests { left: 75px; top: 1078px; font-size: 36px; line-height: 50px; }
  .guests-title { font-size: 40px; font-weight: 600; }
  .location {
    left: 661px; font-size: 32px; font-weight: 600; line-height: 51px;
  }
  .location-top { top: 1150px; }
  .location-bottom { top: 1980px; }
  .polish { left: 105px; top: 2092px; font-size: 40px; line-height: 50px; }
  .polish strong { font-weight: 600; }
</style>
</head>
<body>
  <div class="panel-divider"></div>

  <h1 class="block script deal-title">Door buster Deal !</h1>

  <section class="block offer">
    <h2 class="offer-title">$66 Body Waxing</h2>
    <p>For women only<br>(Neck to Toe -<br>Including Brazilian)<br>with Take Home Scrub<br>used to improve<br>in-grown body hair.</p>
    <p class="offer-value">($120 value)</p>
  </section>

  <div class="block figure-art" role="img" aria-label="Faint line drawing of a slender standing figure"></div>

  <p class="block script call-to-action">Call today<br>to book a spot.</p>

  <div class="body-outline" style="left:4px; top:700px;" role="img" aria-label="Faint line drawing of a reclining body"></div>
  <div class="body-outline" style="left:606px; top:680px;" role="img" aria-label="Faint line drawing of a reclining body"></div>
  <div class="body-outline" style="left:4px; top:1606px;" role="img" aria-label="Faint line drawing of a reclining body"></div>
  <div class="body-outline" style="left:606px; top:1586px;" role="img" aria-label="Faint line drawing of a reclining body"></div>
  <div class="body-outline" style="left:4px; top:2470px;" role="img" aria-label="Faint line drawing of a reclining body"></div>
  <div class="body-outline" style="left:606px; top:2452px;" role="img" aria-label="Faint line drawing of a reclining body"></div>

  <section class="block guests">
    <h2 class="guests-title">Guests receive</h2>
    <p>full body waxing<br>during one appointment<br>on the following areas:<br>butt, hollywood, bikini,<br>underarms, stomach,<br>cleavage, full back,<br>full arms &amp; full legs.</p>
  </section>

  <address class="block location location-top" style="font-style:normal;">
    2240 MAPLEVIEW AVE<br>#5&nbsp; Toronto<br>ON&nbsp; M6R 2K8<br>Opp to Rosewood Bakery<br>(416) 555-0142<br>1 (833) 555-0187
  </address>

  <p class="block polish"><strong>$66</strong> Body Polishing<br>The secret to soft,<br>smooth skin.</p>

  <address class="block location location-bottom" style="font-style:normal;">
    2240 MAPLEVIEW AVE<br>#5&nbsp; Toronto<br>ON&nbsp; M6R 2K8<br>Opp to Rosewood Bakery<br>(416) 555-0142<br>1 (833) 555-0187
  </address>
</body>
</html>
```